Birchway Contracting website

I need a website for my construction. I want customers to see past builds and current projects Something that stands out and reflects awareness, safety, attention to details. I already have a logo designed by Studio Marrowfield
Target Market(s)
Residential and Commercial sectors
Industry/Entity Type
Construction
Logo Text
Birchway Contracting
Colors
EB3D1F
EC4F4E
F09395
F8D3D4
FCEDEE
Requirements
Must have
- My contact info
Nice to have
- Past projects

```html
<!DOCTYPE html>
<html lang="en">
<head>
<meta charset="utf-8">
<title>Birchway Contracting</title>
<link href="https://fonts.googleapis.com/css2?family=Arimo:wght@400;700&display=swap" rel="stylesheet">
<style>
:root{
  --red:#EB3D1F;
  --red-soft:#EC4F4E;
  --pink:#F09395;
  --blush:#F8D3D4;
  --mist:#FCEDEE;
  --ink:#111111;
  --text:#333333;
  --dark:#1d2024;
  --grey-bg:#f3f3f3;
  --placeholder:#e4e1da;
  --white:#ffffff;
}
*{margin:0;padding:0;box-sizing:border-box}
html,body{width:1200px;height:4213px;overflow:hidden}
body{font-family:"Arimo",Arial,sans-serif;color:var(--text);background:var(--white);position:relative}
h1,h2,h3{font-weight:400}
.abs{position:absolute}
.section{position:absolute;left:0;width:1200px}
.label{position:absolute;left:0;width:1200px;text-align:center;font-size:10px;letter-spacing:5px;text-transform:uppercase;color:#666}
.title{position:absolute;left:0;width:1200px;text-align:center;font-weight:400;color:var(--ink)}
.btn{position:absolute;display:flex;align-items:center;justify-content:center;font-size:10px;font-weight:700;text-transform:uppercase;color:var(--white);background:var(--red);letter-spacing:.3px}
.btn.black{background:var(--ink)}
.photo{position:absolute}
.brand{position:absolute;display:flex;align-items:center;gap:10px;color:var(--white);font-weight:700;text-transform:uppercase}
.brand-mark{width:18px;height:18px;background:var(--red)}

/* hero */
.hero{top:0;height:667px;background:linear-gradient(135deg,#5a4a40 0%,#3b3430 45%,#6b5648 75%,#2c2825 100%);clip-path:polygon(0 0,100% 0,100% 569px,50% 667px,0 572px)}
.nav{position:absolute;top:30px;font-size:11px;color:var(--white);text-transform:uppercase}
.nav.active::after{content:"";position:absolute;left:0;right:0;top:25px;height:2px;background:var(--red)}
.nav-line{position:absolute;left:230px;top:62px;width:785px;height:1px;background:rgba(255,255,255,.25)}
.phone-box{position:absolute;left:1015px;top:0;width:185px;height:62px;background:var(--red);display:flex;align-items:center;justify-content:center;gap:12px;color:var(--white);font-size:19px}
.hero-kicker{position:absolute;left:100px;top:240px;font-size:13px;letter-spacing:6px;color:var(--white)}
.hero-title{position:absolute;left:100px;top:265px;font-size:54px;line-height:56px;color:var(--white);font-weight:400}

/* welcome */
.welcome-text{position:absolute;left:566px;width:470px;font-size:10.5px;line-height:17px;color:var(--text)}
.rule{position:absolute;height:2px;background:var(--red)}

/* cards */
.projects-now{top:1316px;height:760px;background:var(--grey-bg)}
.card-photo{position:absolute;width:304px;height:227px}
.card-photo::after{content:"";position:absolute;left:146px;bottom:-9px;border-left:7px solid transparent;border-right:7px solid transparent;border-top:9px solid var(--red)}
.card-title{position:absolute;width:304px;text-align:center;font-size:22px;font-weight:400;color:var(--ink)}
.card-text{position:absolute;width:304px;text-align:center;font-size:10.5px;line-height:17px;padding:0 30px}

/* recent */
.recent{top:1995px;height:554px;background:linear-gradient(180deg,#23272c,#1a1c20 60%,#2a2520);clip-path:polygon(0 95px,50% 0,100% 95px,100% 100%,0 100%)}
.recent-photo{position:absolute;top:194px;width:229px;height:169px}
.recent-name{position:absolute;top:400px;width:229px;text-align:center;font-size:16px;color:var(--white)}

/* services */
.service-icon{position:absolute;width:57px;height:57px;background:var(--blush)}
.service-title{position:absolute;font-size:22px;font-weight:400;color:var(--ink)}
.service-text{position:absolute;width:215px;font-size:10.5px;line-height:17px}

/* contact */
.contact{top:3281px;height:520px;background:var(--red);clip-path:polygon(0 87px,50% 0,100% 87px,100% 100%,0 100%)}
.field{position:absolute;border:2px solid rgba(255,255,255,.75);color:var(--white);font-size:10px;padding:8px 16px}

/* footer */
.footer{top:3801px;height:412px;background:#1b1b1b}
.f-link{position:absolute;left:101px;font-size:10.5px;color:var(--white);text-transform:uppercase}
.f-label{position:absolute;left:336px;font-size:9px;color:#999}
.f-value{position:absolute;left:336px;color:var(--white)}
.social{position:absolute;top:4164px;width:12px;height:12px;border-radius:50%;background:var(--white)}
</style>
</head>
<body>

<header class="section hero">
  <div class="photo" style="left:0;top:0;width:1200px;height:667px" role="img" aria-label="Construction worker in safety gear smoothing concrete on a site"></div>
  <div class="brand" style="left:39px;top:38px;font-size:21px;line-height:22px;width:220px"><span class="brand-mark"></span><span>Birchway<br>Contracting</span></div>
  <div class="nav-line"></div>
  <nav>
    <a class="nav active" style="left:414px">Home</a>
    <a class="nav" style="left:487px">About</a>
    <a class="nav" style="left:566px">Services</a>
    <a class="nav" style="left:661px">Projects</a>
    <a class="nav" style="left:759px">Contact Us</a>
  </nav>
  <div class="phone-box">
    <svg width="20" height="20" viewBox="0 0 24 24"><rect x="0" y="0" width="24" height="24" fill="#111"/><path d="M7 5l3 0 1 4-2 1a9 9 0 0 0 5 5l1-2 4 1 0 3c0 1-1 2-2 2A13 13 0 0 1 5 7c0-1 1-2 2-2z" fill="none" stroke="#fff" stroke-width="1.4"/></svg>
    <span>204-555-0147</span>
  </div>
  <div class="hero-kicker">RESIDENTIAL &nbsp;•COMMERCIAL</div>
  <h1 class="hero-title">Lorem ipsum dolor<br>consectetuer adipiscing.</h1>
  <a class="btn" style="left:100px;top:419px;width:108px;height:31px">Contact Us</a>
</header>

<section class="section" style="top:667px;height:649px">
  <div class="label" style="top:84px">Welcome</div>
  <h2 class="title" style="top:108px;font-size:56px">Birchway Contracting</h2>
  <svg class="abs" style="left:26px;top:165px" width="244" height="82" viewBox="0 0 244 82"><polygon points="0,0 244,0 232,16 40,16 56,80" fill="var(--red)"/></svg>
  <div class="photo" style="left:100px;top:201px;width:400px;height:353px;background:linear-gradient(135deg,#c9a77a,#8a7a66 50%,#d8c6a6)" role="img" aria-label="Aerial view of carpenters cutting timber on a wooden deck"></div>
  <div class="rule" style="left:566px;top:217px;width:68px"></div>
  <p class="welcome-text" style="top:246px">Lorem ipsum dolor sit amet, consectetuer adipiscing elit, sed diam nonummy nibh euismod tincidunt ut laoreet dolore magna aliquam erat volutpat.</p>
  <p class="welcome-text" style="top:297px">Ut wisi enim ad minim veniam, quis nostrud exerci tation ullamcorper suscipit lobortis nisl ut aliquip ex ea commodo consequat. Duis autem vel eum iriure dolor in hendrerit in vulputate velit esse molestie consequat, vel illum dolore eu feugiat nulla facilisis at vero eros et accumsan et iusto odio dignissim qui blandit praesent luptatum zzril delenit augue duis dolore te feugait nulla facilisi.</p>
  <div class="abs" style="left:566px;top:428px;font-size:10px;font-weight:700;color:var(--ink)">Call us at:</div>
  <svg class="abs" style="left:624px;top:421px" width="24" height="24" viewBox="0 0 24 24"><path d="M6 3l4 0 1 5-2 2a10 10 0 0 0 5 5l2-2 5 1 0 4c0 1-1 2-2 2A17 17 0 0 1 4 5c0-1 1-2 2-2z" fill="none" stroke="var(--red)" stroke-width="1.5"/></svg>
  <div class="abs" style="left:658px;top:421px;font-size:22px;color:var(--ink)">204-555-0147</div>
  <a class="btn" style="left:566px;top:471px;width:109px;height:33px">Read More</a>
  <a class="btn black" style="left:687px;top:471px;width:109px;height:33px">Contact Us</a>
  <div class="photo" style="left:826px;top:379px;width:245px;height:197px;background:var(--placeholder)" role="img" aria-label="Safety hard hat product photo"></div>
</section>

<section class="section projects-now">
  <div class="label" style="top:92px">Birchway Contracting</div>
  <h2 class="title" style="top:109px;font-size:52px">Current Projects</h2>

  <div class="card-photo" style="left:100px;top:190px;background:linear-gradient(160deg,#b9c7d4,#8a7a62 60%,#5e5346)" role="img" aria-label="Timber scaffolding against the sky"></div>
  <h3 class="card-title" style="left:100px;top:451px">Laoreet Dolore</h3>
  <p class="card-text" style="left:100px;top:481px">Nostrud exerci tation ullamcorper suscipit lobortis nisl ut aliquip ex ea commodo consequat.</p>
  <a class="btn" style="left:198px;top:545px;width:108px;height:29px">Learn More</a>

  <div class="card-photo" style="left:448px;top:190px;background:linear-gradient(135deg,#7f8b92,#a8b0b2 50%,#5d6468)" role="img" aria-label="Workers tying rebar on a concrete slab"></div>
  <h3 class="card-title" style="left:448px;top:451px">Euismod Tincidunt</h3>
  <p class="card-text" style="left:448px;top:481px">Vel eum iriure dolor in hendrerit in vulputate velit esse molestie consequat vel illum dolore.</p>
  <a class="btn" style="left:546px;top:545px;width:108px;height:29px">Learn More</a>

  <div class="card-photo" style="left:795px;top:190px;background:linear-gradient(180deg,#5aa9e0,#a7b6c2 45%,#7d6d60)" role="img" aria-label="Steel-framed apartment building under construction"></div>
  <h3 class="card-title" style="left:795px;top:451px">Wisi Enim Ad Minim</h3>
  <p class="card-text" style="left:795px;top:481px">Odio dignissim qui blandit praesent luptatum zzril augue duis dolore nulla facilisi.</p>
  <a class="btn" style="left:893px;top:545px;width:108px;height:29px">Learn More</a>
</section>

<section class="section recent">
  <div class="photo" style="left:0;top:0;width:1200px;height:554px" role="img" aria-label="Dim background of a welder at work"></div>
  <div class="label" style="top:95px;color:#bbb">Birchway Contracting</div>
  <h2 class="title" style="top:110px;font-size:54px;color:var(--white)">Recent Projects</h2>
  <div class="recent-photo" style="left:10px;background:linear-gradient(180deg,#8ea9d6,#3b4f7a 55%,#6f7f6a)" role="img" aria-label="Two-storey family house at dusk"></div>
  <div class="recent-photo" style="left:247px;background:linear-gradient(135deg,#d6dde6,#3c4048 55%,#55595f)" role="img" aria-label="Modern dark brick facade"></div>
  <div class="recent-photo" style="left:486px;background:linear-gradient(180deg,#dfe3e4,#b9b5ac 55%,#5f6a5d)" role="img" aria-label="Low modern home in a coastal landscape"></div>
  <div class="recent-photo" style="left:724px;background:linear-gradient(135deg,#f2f2f0,#bdbdbb 55%,#2b2b2b)" role="img" aria-label="Bright open-plan interior with dining table"></div>
  <div class="recent-photo" style="left:963px;background:linear-gradient(160deg,#3f8fd8,#e8e4dc 55%,#c9c3b8)" role="img" aria-label="White apartment block against blue sky"></div>
  <div class="recent-name" style="left:10px">Project Name 1</div>
  <div class="recent-name" style="left:247px">Project Name 2</div>
  <div class="recent-name" style="left:486px">Project Name 3</div>
  <div class="recent-name" style="left:724px">Project Name 4</div>
  <div class="recent-name" style="left:963px">Project Name 5</div>
  <a class="btn" style="left:546px;top:462px;width:108px;height:30px">View More</a>
</section>

<section class="section" style="top:2549px;height:732px">
  <div class="label" style="top:106px">What We Do</div>
  <h2 class="title" style="top:122px;font-size:56px">Our Services</h2>

  <div class="service-icon" style="left:96px;top:240px" role="img" aria-label="Consultancy icon"></div>
  <h3 class="service-title" style="left:96px;top:321px">Consultancy</h3>
  <p class="service-text" style="left:96px;top:361px">Lorem ipsum dolor sit amet, consectetuer adipiscing elit, sed diam nonummy nibh euismod tincidunt ut laoreet dolore magna aliquam volutpat.</p>

  <div class="service-icon" style="left:348px;top:240px" role="img" aria-label="Design icon"></div>
  <h3 class="service-title" style="left:348px;top:321px">Design</h3>
  <p class="service-text" style="left:348px;top:361px">Ut wisi enim ad minim veniam, quis nostrud exerci tation ullamcorper suscipit lobortis nisl ut aliquip ex ea commodo consequat.</p>

  <div class="service-icon" style="left:96px;top:481px" role="img" aria-label="Build icon"></div>
  <h3 class="service-title" style="left:96px;top:561px">Build</h3>
  <p class="service-text" style="left:96px;top:601px">Duis autem vel eum iriure dolor in hendrerit in vulputate velit esse molestie vel illum dolore eu feugiat consequat.</p>

  <div class="service-icon" style="left:348px;top:481px" role="img" aria-label="Project management icon"></div>
  <h3 class="service-title" style="left:348px;top:561px">Project Management</h3>
  <p class="service-text" style="left:348px;top:601px">Dignissim qui blandit praesent luptatum zzril delenit augue duis dolore te feugait nulla facilisi.</p>

  <svg class="abs" style="left:929px;top:206px" width="240" height="82" viewBox="0 0 240 82"><polygon points="0,0 240,0 184,80 200,16 12,16" fill="var(--red)"/></svg>
  <div class="photo" style="left:700px;top:236px;width:399px;height:393px;background:linear-gradient(180deg,#5ea3df,#c4d4df 45%,#e07a3c 75%,#b54a1f)" role="img" aria-label="Two site engineers in hard hats and vests reviewing a site"></div>
</section>

<section class="section contact">
  <div class="photo" style="left:0;top:0;width:1200px;height:520px" role="img" aria-label="Red-tinted background of a hard hat and plans"></div>
  <div class="label" style="top:85px;color:var(--blush)">Get Connected</div>
  <h2 class="title" style="top:104px;font-size:56px;color:var(--white)">Contact Us</h2>
  <div class="field" style="left:239px;top:179px;width:233px;height:31px">Name:</div>
  <div class="field" style="left:481px;top:179px;width:233px;height:31px">Phone:</div>
  <div class="field" style="left:724px;top:179px;width:234px;height:31px">Email:</div>
  <div class="field" style="left:239px;top:220px;width:719px;height:147px">Message / Questions:</div>
  <a class="btn black" style="left:546px;top:399px;width:108px;height:31px">Submit Form</a>
</section>

<footer class="section footer">
  <a class="f-link" style="top:95px">Home</a>
  <a class="f-link" style="top:126px">About</a>
  <a class="f-link" style="top:157px">Services</a>
  <a class="f-link" style="top:188px">Projects</a>
  <a class="f-link" style="top:219px">Contact Us</a>

  <div class="f-label" style="top:95px">phone</div>
  <div class="f-value" style="top:112px;font-size:18px">204-555-0147</div>
  <div class="f-label" style="top:157px">location</div>
  <div class="f-value" style="top:174px;font-size:10.5px">Put Address Here, Put Address Here 123</div>
  <div class="f-label" style="top:211px">email</div>
  <div class="f-value" style="top:226px;font-size:10.5px">email@birchwaycontracting.com</div>

  <div class="brand" style="left:687px;top:95px;font-size:28px;line-height:30px"><span class="brand-mark" style="width:22px;height:22px"></span><span>Birchway<br>Contracting</span></div>
  <p class="abs" style="left:706px;top:181px;width:375px;font-size:10.5px;line-height:17px;color:#ddd">Duis autem vel eum iriure dolor in hendrerit in vulputate velit esse molestie consequat, vel illum dolore eu feugiat nulla facilisis at vero eros et accumsan et iusto odio dignissim qui blandit praesent luptatum zzril delenit augue duis dolore te feugait nulla facilisi.</p>

  <div class="abs" style="left:100px;top:331px;width:1000px;height:1px;background:#444"></div>
  <div class="abs" style="left:100px;top:366px;font-size:10px;color:var(--white)">©2022. Birchway Contracting. All Rights Reserved</div>
</footer>
<span class="social" style="left:988px"></span>
<span class="social" style="left:1035px"></span>
<span class="social" style="left:1086px"></span>

</body>
</html>
```